Graphic Design For Website Banner + 4 Product Images - More Work To Follow

We are in the process of launching a new website. I need to design a banner for the homepage, as well as some graphics for my product images.

Please find attached -

1) My current logo.
2) Banner Sample + Product Image Sample - both of these are a screenshot from a common website that I like the design and style of.
3) Colour Scheme Sample 1 - saved image showing colour scheme for Brushwillow that I like.
4) Colour Scheme Sample 2 - Saved image showing colour scheme for Tarlo that I like.
5) Sample 1-4 - These are colour palette samples I created online showing what I like.
6) 4 blank product images to show what is required in the design.

To summarise I'll like to create a banner design and product images similar to what's been attached and have a consistent colour theme throughout. I'm happy to adjust the colours in my logo to match the final designs.

To begin with I'll be requesting 1 banner design and 4 product images. I'll have more work for the successful designer.

Banner -
Size to be 950x300. To contain the following wording -
Quality Printing
Offset|Digital|Wideformat
Deal Direct & Save
Possibly include some product images like the sample banner attached.

Product Images -
Size to be 263x263
1) Business Cards
2) Folded Brochures
3) Flyers
4) Presentation Folders
I've attached blank sample images of all 4 for your reference.

Please feel free to ask any questions as I'm happy to give further direction.

Target Market(s)

We are a commercial Printer offering a range of printed products

Font styles to use
Serif
Sans Serif

Colors
34a6d7
33b8a4
3277b5
86cfc7
86cae7
85acd3
00a990
0393ce
0255a3

```html
<!DOCTYPE html>
<html lang="en">
<head>
<meta charset="utf-8">
<title>Inkmill Press – Banner and Product Samples</title>
<link rel="stylesheet" href="https://fonts.googleapis.com/css2?family=Montserrat:wght@300;400;700;800&family=Open+Sans:wght@400;600&family=Dosis:wght@400&display=swap">
<style>
  :root {
    --board: #262626;
    --board-text: #ffffff;
    --white: #ffffff;
    --paper: #f7f8f8;
    --paper-shade: #e9ecec;
    --ink: #222222;
    --nav-text: #444444;
    --brand-blue: #0393ce;
    --brand-deep: #0255a3;
    --brand-sky: #34a6d7;
    --brand-teal: #33b8a4;
    --hero-start: #2f9dd9;
    --hero-end: #8ccbbc;
    --icon-green: #78b34a;
    --icon-blue: #2a8fd0;
    --icon-teal: #4fb3a0;
    --icon-emerald: #2f9e72;
    --photo-light: #eef0f1;
    --photo-mid: #d9dcde;
    --tile-blue: #3aa6d2;
    --tile-teal: #4a9a97;
    --tile-pink: #efcfd3;
    --tile-lilac: #e5e0e7;
    --tile-mint: #d3ebd5;
    --desk-grey: #e4e8ea;
  }
  * { box-sizing: border-box; margin: 0; padding: 0; }
  html, body { width: 1200px; height: 2200px; overflow: hidden; background: var(--board); }
  body { position: relative; font-family: "Open Sans", sans-serif; }

  .section-title {
    position: absolute; left: 87px; color: var(--board-text);
    font-family: "Montserrat", sans-serif; font-weight: 300; font-size: 29px; letter-spacing: 1px; line-height: 1;
  }
  .board-footer {
    position: absolute; left: 0; width: 1200px; top: 2105px; text-align: center;
    color: var(--board-text); font-family: "Montserrat", sans-serif; font-weight: 300;
    font-size: 28px; letter-spacing: 20px; line-height: 1;
  }

  .site { position: absolute; left: 86px; width: 1027px; height: 515px; background: var(--white); overflow: hidden; }
  .site-nav { position: absolute; left: 0; top: 0; width: 100%; height: 70px; border-bottom: 1px solid #e6e6e6; }
  .nav-brand { position: absolute; left: 124px; top: 24px; font-family: "Montserrat", sans-serif; font-weight: 700; font-size: 15px; color: var(--brand-sky); letter-spacing: 0.5px; }
  .nav-links { position: absolute; left: 308px; top: 16px; display: flex; gap: 12px; font-size: 10px; color: var(--nav-text); }
  .nav-links .is-active { color: var(--brand-blue); }
  .nav-cta { position: absolute; left: 784px; top: 8px; width: 138px; height: 31px; border: 1px solid var(--brand-blue); color: var(--brand-blue); font-family: "Dosis", sans-serif; font-size: 9px; display: flex; align-items: center; justify-content: center; }
  .nav-login { position: absolute; left: 800px; top: 44px; font-size: 7.5px; color: var(--nav-text); }
  .nav-login b { color: var(--brand-blue); }

  .hero { position: absolute; left: 0; top: 70px; width: 100%; height: 326px; overflow: hidden; }
  .hero--gradient { background: linear-gradient(90deg, var(--hero-start) 0%, #5bb2cc 50%, var(--hero-end) 100%); }
  .hero--light { background: linear-gradient(90deg, #ffffff 0%, #f4f6f7 40%, var(--photo-light) 100%); }

  .hero-brand { position: absolute; font-family: "Montserrat", sans-serif; font-weight: 800; line-height: 1.02; }
  .hero--gradient .hero-brand { left: 80px; top: 98px; font-size: 52px; color: var(--white); }
  .hero--light .hero-brand { left: 62px; top: 40px; font-size: 44px; color: var(--brand-sky); }

  .hero-divider { position: absolute; left: 476px; top: 114px; width: 2px; height: 100px; background: var(--white); }

  .hero-copy { position: absolute; font-family: "Montserrat", sans-serif; line-height: 1.2; }
  .hero-copy .headline { font-weight: 800; font-size: 28px; letter-spacing: 1px; }
  .hero-copy .line { font-weight: 400; font-size: 20px; margin-top: 6px; }
  .hero--gradient .hero-copy { left: 604px; top: 120px; color: var(--white); }
  .hero--light .hero-copy { left: 59px; top: 200px; }
  .hero--light .headline { color: var(--brand-deep); }
  .hero--light .line--formats { color: var(--ink); }
  .hero--light .line--save { color: var(--brand-blue); }

  .hero-photo { position: absolute; background: linear-gradient(135deg, rgba(255,255,255,0.9), rgba(236,242,243,0.7)); box-shadow: 0 3px 8px rgba(0,0,0,0.08); }
  .hero-photo--cards-top { left: 470px; top: 24px; width: 180px; height: 104px; transform: rotate(-18deg); }
  .hero-photo--cards-right { left: 900px; top: 40px; width: 100px; height: 80px; transform: rotate(12deg); }
  .hero-photo--cards-low { left: 480px; top: 240px; width: 120px; height: 110px; transform: rotate(-20deg); }
  .hero-photo--flyers { left: 840px; top: 218px; width: 150px; height: 130px; transform: rotate(10deg); }
  .hero-photo--desk { left: 440px; top: 0; width: 587px; height: 326px; box-shadow: none; background: linear-gradient(100deg, rgba(238,240,241,0) 0%, var(--photo-light) 18%, var(--photo-mid) 100%); }

  .features { position: absolute; left: 0; top: 396px; width: 100%; height: 119px; }
  .feature { position: absolute; top: 0; width: 160px; height: 119px; margin-left: -80px; text-align: center; }
  .feature svg { position: absolute; left: 54px; top: 30px; }
  .feature-label { position: absolute; left: 0; width: 100%; top: 98px; font-family: "Dosis", sans-serif; font-size: 12.5px; line-height: 1; }
  .feature--pricing { left: 196px; color: var(--icon-green); }
  .feature--quality { left: 408px; color: var(--icon-blue); }
  .feature--quotes { left: 619px; color: var(--icon-teal); }
  .feature--order { left: 830px; color: var(--icon-emerald); }

  .product-tile { position: absolute; width: 308px; height: 308px; overflow: hidden; }
  .product-tile--brochure { left: 87px; top: 1361px; background: linear-gradient(135deg, #2f9ed6 0%, var(--tile-blue) 50%, #6ab9c9 100%); }
  .product-tile--cards { left: 446px; top: 1361px; background: linear-gradient(135deg, #4f9f9b, var(--tile-teal)); }
  .product-tile--flyers { left: 804px; top: 1361px; background: linear-gradient(135deg, var(--tile-pink), #f4dde0 60%, #eef1f4 100%); }
  .product-tile--notepad { left: 272px; top: 1738px; background: linear-gradient(135deg, var(--tile-lilac), #eeeaf0); }
  .product-tile--folder { left: 630px; top: 1738px; background: linear-gradient(135deg, var(--tile-mint), #e0f1e1); }

  .print-item {
    position: absolute; background: linear-gradient(135deg, var(--white), var(--paper) 60%, var(--paper-shade));
    box-shadow: 0 8px 18px rgba(0,0,0,0.18);
    display: flex; align-items: center; justify-content: center;
  }
  .print-name {
    font-family: "Montserrat", sans-serif; font-weight: 700; font-size: 11px; line-height: 1.05;
    color: var(--brand-sky); letter-spacing: 0.5px; text-align: left;
  }
  .print-name--faint { color: #b9dbe9; }
  .desk-item { position: absolute; background: var(--desk-grey); }

  .brochure-open { left: 88px; top: 70px; width: 190px; height: 140px; transform: rotate(-18deg); }
  .brochure-open::before, .brochure-open::after { content: ""; position: absolute; top: 0; bottom: 0; width: 1px; background: #dde2e3; }
  .brochure-open::before { left: 33%; }
  .brochure-open::after { left: 66%; }
  .brochure-panel { left: 30px; top: 120px; width: 100px; height: 160px; transform: rotate(-35deg); }

  .card-stack { left: 48px; top: 28px; width: 190px; height: 112px; transform: rotate(-5deg); box-shadow: 0 6px 0 #eceeee, 0 12px 18px rgba(0,0,0,0.2); }
  .card-loose { left: 72px; top: 150px; width: 200px; height: 118px; transform: rotate(32deg); }

  .flyer-back { left: 112px; top: 40px; width: 110px; height: 170px; transform: rotate(-10deg); }
  .flyer-front { left: 30px; top: 40px; width: 130px; height: 180px; transform: rotate(-30deg); }
  .keyboard { left: 40px; top: 250px; width: 300px; height: 80px; transform: rotate(-12deg); }
  .pen { left: 236px; top: 60px; width: 8px; height: 150px; transform: rotate(-8deg); background: #c9cdcf; }

  .notepad { left: 88px; top: 56px; width: 200px; height: 240px; transform: rotate(-14deg); align-items: flex-end; justify-content: flex-end; padding: 0 24px 30px 0; border-top: 6px solid #cfd2d6; }
  .lavender { left: 10px; top: 20px; width: 150px; height: 36px; transform: rotate(-10deg); background: #b3b8cf; }

  .folder-back { left: 160px; top: 20px; width: 130px; height: 170px; transform: rotate(-35deg); }
  .folder-front { left: 30px; top: 110px; width: 170px; height: 210px; transform: rotate(-35deg); }
</style>
</head>
<body>

  <h2 class="section-title" style="top:74px;">BANNER_SAMPLE 1</h2>

  <section class="site" style="top:120px;">
    <header class="site-nav">
      <div class="nav-brand">INKMILL PRESS</div>
      <nav class="nav-links"><span class="is-active">Home</span><span>About</span><span>Products</span><span>Support</span><span>Contact</span></nav>
      <div class="nav-cta">REGISTER &amp; SHOP NOW</div>
      <div class="nav-login">Already have an account? <b>Log in</b></div>
    </header>
    <div class="hero hero--gradient">
      <div class="hero-photo hero-photo--cards-top" role="img" aria-label="Photo of branded folders and business cards"></div>
      <div class="hero-photo hero-photo--cards-right" role="img" aria-label="Photo of stacked business cards"></div>
      <div class="hero-photo hero-photo--cards-low" role="img" aria-label="Photo of folded brochures"></div>
      <div class="hero-photo hero-photo--flyers" role="img" aria-label="Photo of printed flyers"></div>
      <div class="hero-brand">INKMILL<br>PRESS</div>
      <div class="hero-divider"></div>
      <div class="hero-copy">
        <div class="headline">QUALITY PRINTING</div>
        <div class="line">OFFSET | DIGITAL | WIDEFORMAT</div>
        <div class="line">DEAL DIRECT &amp; SAVE</div>
      </div>
    </div>
    <div class="features">
      <div class="feature feature--pricing">
        <svg width="52" height="52" viewBox="0 0 50 50" fill="none" stroke="currentColor" stroke-width="2"><path d="M4 6 L22 4 L46 28 L28 46 L4 22 Z"/><circle cx="14" cy="14" r="4"/><path d="M24 34 L34 24 M28 38 L38 28"/></svg>
        <span class="feature-label">FANTASTIC PRICING</span>
      </div>
      <div class="feature feature--quality">
        <svg width="52" height="56" viewBox="0 0 50 54" fill="none" stroke="currentColor" stroke-width="2"><path d="M12 4 H38 V20 Q38 36 25 38 Q12 36 12 20 Z"/><path d="M12 10 Q2 12 6 24 Q9 30 14 30 M38 10 Q48 12 44 24 Q41 30 36 30"/><path d="M25 38 V46 M17 48 H33 M15 52 H35"/></svg>
        <span class="feature-label">QUALITY PRINTING</span>
      </div>
      <div class="feature feature--quotes">
        <svg width="52" height="52" viewBox="0 0 52 52" fill="none" stroke="currentColor" stroke-width="2"><circle cx="26" cy="26" r="23"/><path d="M26 10 V27 H40"/></svg>
        <span class="feature-label">INSTANT QUOTES</span>
      </div>
      <div class="feature feature--order">
        <svg width="52" height="52" viewBox="0 0 52 52" fill="none" stroke="currentColor" stroke-width="2"><path d="M16 20 L24 4 M36 20 L28 4"/><path d="M4 20 H48 V26 H4 Z"/><path d="M7 26 L10 48 H42 L45 26"/><path d="M16 32 V42 M22 32 V42 M28 32 V42 M34 32 V42"/></svg>
        <span class="feature-label">EASY TO ORDER</span>
      </div>
    </div>
  </section>

  <section class="site" style="top:703px;">
    <header class="site-nav">
      <div class="nav-brand">INKMILL PRESS</div>
      <nav class="nav-links"><span class="is-active">Home</span><span>About</span><span>Products</span><span>Support</span><span>Contact</span></nav>
      <div class="nav-cta">REGISTER &amp; SHOP NOW</div>
      <div class="nav-login">Already have an account? <b>Log in</b></div>
    </header>
    <div class="hero hero--light">
      <div class="hero-photo hero-photo--desk" role="img" aria-label="Photo of a white stationery flat lay with tablet, mug, notebooks and bags"></div>
      <div class="hero-brand">INKMILL<br>PRESS</div>
      <div class="hero-copy">
        <div class="headline">QUALITY PRINTING</div>
        <div class="line line--formats">OFFSET | DIGITAL | WIDEFORMAT</div>
        <div class="line line--save">DEAL DIRECT &amp; SAVE</div>
      </div>
    </div>
    <div class="features">
      <div class="feature feature--pricing">
        <svg width="52" height="52" viewBox="0 0 50 50" fill="none" stroke="currentColor" stroke-width="2"><path d="M4 6 L22 4 L46 28 L28 46 L4 22 Z"/><circle cx="14" cy="14" r="4"/><path d="M24 34 L34 24 M28 38 L38 28"/></svg>
        <span class="feature-label">FANTASTIC PRICING</span>
      </div>
      <div class="feature feature--quality">
        <svg width="52" height="56" viewBox="0 0 50 54" fill="none" stroke="currentColor" stroke-width="2"><path d="M12 4 H38 V20 Q38 36 25 38 Q12 36 12 20 Z"/><path d="M12 10 Q2 12 6 24 Q9 30 14 30 M38 10 Q48 12 44 24 Q41 30 36 30"/><path d="M25 38 V46 M17 48 H33 M15 52 H35"/></svg>
        <span class="feature-label">QUALITY PRINTING</span>
      </div>
      <div class="feature feature--quotes">
        <svg width="52" height="52" viewBox="0 0 52 52" fill="none" stroke="currentColor" stroke-width="2"><circle cx="26" cy="26" r="23"/><path d="M26 10 V27 H40"/></svg>
        <span class="feature-label">INSTANT QUOTES</span>
      </div>
      <div class="feature feature--order">
        <svg width="52" height="52" viewBox="0 0 52 52" fill="none" stroke="currentColor" stroke-width="2"><path d="M16 20 L24 4 M36 20 L28 4"/><path d="M4 20 H48 V26 H4 Z"/><path d="M7 26 L10 48 H42 L45 26"/><path d="M16 32 V42 M22 32 V42 M28 32 V42 M34 32 V42"/></svg>
        <span class="feature-label">EASY TO ORDER</span>
      </div>
    </div>
  </section>

  <h2 class="section-title" style="top:1244px;">BANNER_SAMPLE 2</h2>

  <div class="product-tile product-tile--brochure" role="img" aria-label="Product photo of a tri-fold brochure on a blue background">
    <div class="print-item brochure-open"><span class="print-name">INKMILL<br>PRESS</span></div>
    <div class="print-item brochure-panel"><span class="print-name">INKMILL<br>PRESS</span></div>
  </div>

  <div class="product-tile product-tile--cards" role="img" aria-label="Product photo of business cards on a teal background">
    <div class="print-item card-stack"><span class="print-name">INKMILL<br>PRESS</span></div>
    <div class="print-item card-loose"><span class="print-name">INKMILL<br>PRESS</span></div>
  </div>

  <div class="product-tile product-tile--flyers" role="img" aria-label="Product photo of flyers with a pen and keyboard on a pink desk">
    <div class="desk-item keyboard"></div>
    <div class="print-item flyer-back"><span class="print-name">INKMILL<br>PRESS</span></div>
    <div class="print-item flyer-front"><span class="print-name">INKMILL<br>PRESS</span></div>
    <div class="desk-item pen"></div>
  </div>

  <div class="product-tile product-tile--notepad" role="img" aria-label="Product photo of a spiral notepad with lavender and pen">
    <div class="desk-item lavender"></div>
    <div class="print-item notepad"><span class="print-name">INKMILL<br>PRESS</span></div>
  </div>

  <div class="product-tile product-tile--folder" role="img" aria-label="Product photo of a presentation folder on a mint background">
    <div class="print-item folder-back"><span class="print-name">INKMILL<br>PRESS</span></div>
    <div class="print-item folder-front"><span class="print-name print-name--faint">INKMILL<br>PRESS</span></div>
  </div>

  <div class="board-footer">PRODUCT SAMPLE</div>

</body>
</html>
```